Brochure Design Project

1.We need a brochure design for our event program and invitation.

2.We must be able to print out the brochure and also send it out via email to participants.

3.We want the whole design to relate to "Cross-Examination","International Arbitration" atmosphere.

4.We want the design to look a bit (but not too) fancy and be readable.

Reason: There are only 2 of 6 designs we like. But we still need more options to choose.

Target Market(s)

Our audiences are all Chinese and International Lawyers

Industry/Entity Type

Event

Requirements
Must have
• 1. The brochure needs to actually reflect “cross-examination” on the cover. The title should go at the top of the page.

2. The brochure needs to make room for organizers and supporters’ logo. This is a cooperation event.

3. It is important that the text is a big enough to be read easily. At the moment we have been using Helvetica font at size 9 or 10. Helvetica is easily readable at this size.

4. The brochure color needs to be in line with our logo color, such as Green-Blue and white. Please suggest a color that also fits the organizers’ logo.

5. We need a pdf version and print out version. They are all A4 size. The pdf version size must be under 2 MB. Otherwise it’s difficult to send out as well as receive. For the printing version, when designing you need to leave a 4mm bleed over the page size. This bleed is important - otherwise the picture will not necessarily go to the edge of the cut. You also need to make sure that the text is not too close to the boundary. I tend to leave a 4-5mm margin for text within this on all sides.

6. Use the same font style as suggested in the draft program and invitation.
Nice to have
• A picture which represents the idea of cross-examination. I will send you the example pic.
Should not have
• 1. Should not be aggressive;

2. Should not be too fancy or too conservative;

3. Should not be too colorful

```html
<!DOCTYPE html>
<html lang="en">
<head>
<meta charset="utf-8">
<title>Cross Examination in International Arbitration – Workshop Brochure</title>
<link rel="stylesheet" href="https://fonts.googleapis.com/css2?family=Roboto:wght@300;400;700;900&family=Arimo:wght@400;700&family=Crimson+Text:ital@1&display=swap">
<style>
  :root {
    --teal: #17708e;
    --teal-dark: #0f5b75;
    --red: #b3282d;
    --ink: #1c1c1c;
    --rule: #d4d4d4;
    --paper: #ffffff;
    --backdrop: #e5e5e5;
  }
  * { box-sizing: border-box; margin: 0; padding: 0; }
  html, body { width: 1200px; height: 702px; overflow: hidden; }
  body { background: var(--backdrop); position: relative; font-family: "Arimo", Arial, sans-serif; color: var(--ink); }

  /* ---------- Inside spread ---------- */
  .spread {
    position: absolute; left: 414px; top: 150px; width: 746px; height: 528px;
    background: var(--paper); display: flex;
  }
  .spread-page { position: relative; width: 50%; height: 100%; }
  .spread-page + .spread-page { border-left: 1px solid #ececec; }
  .page-band { position: absolute; left: 0; top: 0; width: 100%; height: 73px; overflow: hidden; background: var(--teal); }
  .page-band svg { position: absolute; inset: 0; width: 100%; height: 100%; }
  .page-title {
    position: absolute; top: 26px; font-family: "Roboto", sans-serif; font-weight: 900;
    font-size: 20px; color: #fff; letter-spacing: 0.1px;
  }
  .program .page-title { left: 27px; }
  .course .page-title { left: 26px; }

  .language-note {
    position: absolute; top: 80px; right: 13px; font-family: "Crimson Text", serif;
    font-style: italic; font-size: 6.8px; color: var(--ink);
  }
  .flag { position: absolute; width: 22px; height: 22px; }
  .day-heading {
    position: absolute; left: 47px; width: 294px; font-family: "Roboto", sans-serif; font-weight: 300;
    font-size: 15.5px; color: var(--teal); border-bottom: 1px solid var(--rule); padding-bottom: 3px;
  }
  .schedule { position: absolute; left: 48px; list-style: none; font-size: 6.9px; }
  .schedule li { display: flex; align-items: baseline; height: 12.5px; }
  .slot { display: flex; width: 70px; flex-shrink: 0; }
  .slot .leader { flex: 1; border-bottom: 1px dotted #777; margin: 0 1px 1.5px; }
  .activity.key { font-weight: 700; }

  .aim-flag { position: absolute; left: 1px; top: 92px; width: 42px; height: 25px; }
  .aim-heading {
    position: absolute; left: 54px; top: 96px; width: 296px; font-family: "Roboto", sans-serif;
    font-weight: 300; font-size: 15px; color: var(--teal); border-bottom: 1px solid var(--rule); padding-bottom: 3px;
  }
  .course-text {
    position: absolute; left: 22px; top: 135px; width: 328px; font-size: 6.5px; line-height: 8.8px;
    text-align: justify;
  }
  .course-text p { margin-bottom: 9.5px; }
  .course-text strong { font-weight: 700; }

  /* ---------- Cover ---------- */
  .cover {
    position: absolute; left: 58px; top: 37px; width: 373px; height: 528px; background: var(--paper);
  }
  .cover-band { position: absolute; left: 0; top: 19px; width: 100%; height: 160px; overflow: hidden; background: var(--teal); }
  .cover-band svg { position: absolute; inset: 0; width: 100%; height: 100%; }
  .cover-photo {
    position: absolute; left: 0; top: 0; width: 100%; height: 100%;
    background: linear-gradient(100deg, #3a3a3a 0%, #8d8d8d 20%, #cfcfcf 45%, #e9e9e9 62%, #9a9a9a 88%, #5c5c5c 100%);
    clip-path: polygon(100px 0, 373px 0, 373px 160px, 22px 160px);
  }
  .cover-title {
    position: absolute; top: 204px; left: 0; width: 100%; text-align: center;
    font-family: "Roboto", sans-serif; font-weight: 700; font-size: 22.5px; line-height: 25px; color: var(--teal);
  }
  .cover-subtitle {
    position: absolute; top: 256px; left: 0; width: 100%; text-align: center;
    font-family: "Crimson Text", serif; font-style: italic; font-size: 11px;
  }
  .cover-rule { position: absolute; left: 88px; width: 196px; border-top: 1px solid var(--rule); }
  .cover-info { position: absolute; left: 0; width: 100%; text-align: center; font-size: 9.2px; line-height: 11px; }
  .cover-info strong { font-weight: 700; }
  .credit-label {
    position: absolute; left: 24px; font-family: "Crimson Text", serif; font-style: italic; font-size: 7.2px;
  }
  .org-name { position: absolute; font-family: "Roboto", sans-serif; font-weight: 700; }
  .org-kestrel { left: 69px; top: 437px; font-size: 13px; color: var(--teal); }
  .org-harbor { left: 214px; top: 440px; font-size: 8.5px; color: var(--ink); }
  .cover-foot { position: absolute; left: 0; bottom: 0; width: 100%; height: 13px; background: var(--teal); overflow: hidden; }
  .cover-foot svg { width: 100%; height: 100%; display: block; }
</style>
</head>
<body>

<!-- Inside spread -->
<section class="spread">
  <div class="spread-page program">
    <div class="page-band">
      <svg viewBox="0 0 373 73" preserveAspectRatio="none" aria-hidden="true">
        <polygon points="160,0 260,0 230,73 200,73" fill="#136684"/>
        <polygon points="260,0 373,0 373,73 230,73" fill="#1a7593"/>
        <polygon points="0,0 70,0 40,73 0,73" fill="#136684"/>
      </svg>
      <h2 class="page-title">Program.</h2>
    </div>
    <p class="language-note">This workshop will be conducted in English</p>

    <svg class="flag" style="left:8px; top:128px;" viewBox="0 0 22 22" aria-hidden="true">
      <polygon points="0,0 22,0 17,11 22,22 0,22" fill="var(--red)"/>
      <rect x="6" y="7" width="7" height="7" fill="none" stroke="#fff" stroke-width="1"/>
      <line x1="6" y1="9" x2="13" y2="9" stroke="#fff" stroke-width="1"/>
    </svg>
    <h3 class="day-heading" style="top:131px;">10 December, 2012</h3>
    <ol class="schedule" style="top:160px;">
      <li><span class="slot">8:30 - 9:00<span class="leader"></span></span><span class="activity">Registration</span></li>
      <li><span class="slot">9:00 - 9:15<span class="leader"></span></span><span class="activity key">Introductory words by Harbor Point and Kestrelwood</span></li>
      <li><span class="slot">9:15 - 9:25<span class="leader"></span></span><span class="activity key">Demonstration of direct examination</span></li>
      <li><span class="slot">9:25 - 9:45<span class="leader"></span></span><span class="activity key">Demonstration of cross-examination</span></li>
      <li><span class="slot">9:45 - 10:15<span class="leader"></span></span><span class="activity key">Case strategy: Preparation for cross</span></li>
      <li><span class="slot">10:15 - 10:30<span class="leader"></span></span><span class="activity">Coffee Break</span></li>
      <li><span class="slot">10:30 - 12:00<span class="leader"></span></span><span class="activity key">Exercises in classic cross-examination</span></li>
      <li><span class="slot">12:00 - 12:15<span class="leader"></span></span><span class="activity key">Instructor and student observations on exercises</span></li>
      <li><span class="slot">12:15 - 13:15<span class="leader"></span></span><span class="activity">Lunch</span></li>
      <li><span class="slot">13:15 - 14:45<span class="leader"></span></span><span class="activity key">Exercises in classic cross-examination</span></li>
      <li><span class="slot">14:45 - 15:00<span class="leader"></span></span><span class="activity">Coffee Break</span></li>
      <li><span class="slot">15:00 - 15:30<span class="leader"></span></span><span class="activity key">Demonstration of cross-examination of experts</span></li>
      <li><span class="slot">15:30 - 17:30<span class="leader"></span></span><span class="activity key">Exercises in expert cross-examination</span></li>
      <li><span class="slot">19.00 - 21:30<span class="leader"></span></span><span class="activity">Joint dinner sponsored by Kestrelwood</span></li>
    </ol>

    <svg class="flag" style="left:8px; top:354px;" viewBox="0 0 22 22" aria-hidden="true">
      <polygon points="0,0 22,0 17,11 22,22 0,22" fill="var(--red)"/>
      <rect x="6" y="7" width="7" height="7" fill="none" stroke="#fff" stroke-width="1"/>
      <line x1="6" y1="9" x2="13" y2="9" stroke="#fff" stroke-width="1"/>
    </svg>
    <h3 class="day-heading" style="top:357px;">11 December, 2012</h3>
    <ol class="schedule" style="top:386px;">
      <li><span class="slot">9:00 - 10:30<span class="leader"></span></span><span class="activity key">Repeat weak spots, dealing with different panels</span></li>
      <li><span class="slot">10:30 - 10:50<span class="leader"></span></span><span class="activity key">Demonstration of “hot-tubbing” expert witnesses</span></li>
      <li><span class="slot">10:50 - 11:00<span class="leader"></span></span><span class="activity">Coffee Break</span></li>
      <li><span class="slot">11:00 - 12:30<span class="leader"></span></span><span class="activity key">Exercises in expert cross-examination</span></li>
    </ol>
  </div>

  <div class="spread-page course">
    <div class="page-band">
      <svg viewBox="0 0 373 73" preserveAspectRatio="none" aria-hidden="true">
        <polygon points="0,0 110,0 80,73 0,73" fill="#136684"/>
        <polygon points="240,0 373,0 373,73 280,73" fill="#1a7593"/>
      </svg>
      <h2 class="page-title">General Course Description.</h2>
    </div>

    <svg class="aim-flag" viewBox="0 0 42 25" aria-hidden="true">
      <polygon points="0,0 42,0 36,12.5 42,25 0,25" fill="var(--red)"/>
      <circle cx="15" cy="10" r="4" fill="none" stroke="#fff" stroke-width="2" stroke-dasharray="2 1.2"/>
      <circle cx="15" cy="10" r="1.3" fill="#fff"/>
      <circle cx="23" cy="17" r="3" fill="none" stroke="#fff" stroke-width="1.6" stroke-dasharray="1.6 1"/>
    </svg>
    <h3 class="aim-heading">Aim of the Course</h3>

    <div class="course-text">
      <p>The goal of the course is to give learning-by-doing training in cross-examination for lawyers and experts from civil law countries, who may have limited opportunity to learn cross-examination in their domestic practice.</p>
      <p>The course is for 1.5 days and is divided into three sub-parts:</p>
      <p><strong>1st Session</strong> (1st Day - Morning Session): The first session is dedicated to learning the basics of cross-examination, including how to prepare the expert for the cross.</p>
      <p><strong>2nd Session</strong> (1st Day - Afternoon Session): The second session is dedicated to doing practical exercises of cross-examination.</p>
      <p><strong>3rd Session</strong> (2nd Day - Morning Session): The third session is dedicated to repeating weak spots and also to learning new forms of expert examination, such as ‘hot tubbing’ or ‘witness conferencing’.</p>
      <p>Participants are limited to a maximum number of 32 and are divided into four groups: two are assigned the role of the Claimant and the other two the role of the Respondent. Each group has a maximum of 8 participants, among which 6-7 act as the party’s counsel and 1-2 participants act as the Experts appointed by such party. These assignments remain throughout the course. Each group is coached by a team of three instructors (i.e. 3 instructors for 8 participants).</p>
      <p>While there are some lectures and demonstrations, the vast majority of the course is dedicated to having the participants do cross-examination. Each participant acting as counsel will do at least one cross-examination and be a witness at least once (being a witness is also a valuable part of the learning experience, as is watching the other participants.). Each participant acting as Expert will be subject to at least two cross-examinations by the participants acting as counsel. Each cross-examination lasts from 10 to 14 minutes and each participant is videotaped.</p>
      <p>Two instructors give brief critiques after each Exercise. In addition, each participant will receive individual comments from a third instructor using the videotape of the participant’s performance (this is often the most effective part of the training).</p>
      <p>The faculty consists of experienced instructors from the US, most of whom have also taught abroad, but also instructors from Asia and Europe, who have extensive experience acting as counsel or arbitrators in international arbitration proceedings. This diversity in background and experience ensures that the participants are exposed to the different approaches that an arbitral tribunal may take to cross examination, depending on the background and nationality of the individual arbitrators.</p>
      <p>To make the exercise as realistic as possible, the course is based on a real case adapted to the needs of the exercise. The participants are given the case in advance (contracts, correspondence, demand for arbitration and response, witness statements, expert witness reports, etc.) for them to prepare.</p>
    </div>
  </div>
</section>

<!-- Cover -->
<section class="cover">
  <div class="cover-band">
    <svg viewBox="0 0 373 160" preserveAspectRatio="none" aria-hidden="true">
      <polygon points="0,0 60,0 0,120" fill="#136684"/>
      <polygon points="92,0 100,0 22,160 14,160" fill="#ffffff"/>
    </svg>
    <div class="cover-photo" role="img" aria-label="Black-and-white photograph of a witness seen in silhouette, seated at a hearing table beside a window"></div>
  </div>

  <h1 class="cover-title">Cross Examination<br>in International Arbitration</h1>
  <p class="cover-subtitle">A Learn-by-Doing Workshop for Lawyers &amp; Experts</p>
  <div class="cover-rule" style="top:286px;"></div>

  <p class="cover-info" style="top:303px;"><strong>Kestrelwood Advisory</strong> &amp;<br><strong>Harbor Point Chambers International LLC</strong><br>International Arbitration Seminars &amp; Workshops</p>
  <p class="cover-info" style="top:353px;">Hosted by<br><strong>Eastgate Dispute Commission, Lanting District, Beijing</strong><br>December 10-11, 2012</p>
  <div class="cover-rule" style="top:402px;"></div>

  <span class="credit-label" style="top:445px;">Organizers:</span>
  <span class="org-name org-kestrel">Kestrelwood Advisory</span>
  <span class="org-name org-harbor">Harbor Point Chambers</span>
  <span class="credit-label" style="top:484px;">Supporters:</span>

  <div class="cover-foot">
    <svg viewBox="0 0 373 13" preserveAspectRatio="none" aria-hidden="true">
      <polygon points="0,0 120,0 110,13 0,13" fill="#136684"/>
      <polygon points="280,0 373,0 373,13 290,13" fill="#0f5b75"/>
    </svg>
  </div>
</section>

</body>
</html>
```